Floral Perfume Box Project for a high end boutique perfumery

I would like a design for a perfume box that has the following flowers on it: Gardenia, Lily of the valley, Freesia, jasmine, Rose. Metalic, gold highlights would be nice. The box should have a modern artistic look with both embossed and raised designs. Combine the Valcourt Perfume (Miss Valcourt) with the Brumel tessavine box

Target Market(s)

Women ready to be married: This perfume is a wedding day scent

Industry/Entity Type

Boutique

Font styles to use
Sans Serif
Decorative

Colors

Designer to choose colors to be used in the design.

Requirements
Must have
• Similar design to Valcourt , please see the Valcourt Perfume images.
• The box must be white. The details should be done to the flowers with gold and silver high lights we will be using foil printing.
Nice to have
• gold highlights would be nice. The box should have a modern artistic look with both embossed and raised designs.
Should not have
• The box cannot be colored it must be white . The best art will be determined by the details of the flowers.

```html
<!DOCTYPE html>
<html lang="en">
<head>
<meta charset="utf-8">
<title>Floral Perfume Box – Front Panel</title>
<link href="https://fonts.googleapis.com/css2?family=Josefin+Sans:wght@300&family=Kaushan+Script&display=swap" rel="stylesheet">
<style>
  :root {
    --backdrop: #e4e4e6;
    --box-white: #ffffff;
    --ink: #111111;
    --frame-line: #2a2a2a;
    --petal-white: #f7f4ea;
    --petal-cream: #efe6c6;
    --foil-gold: #d9bf7a;
    --leaf-light: #a9c46e;
    --leaf-green: #7fa34c;
    --leaf-deep: #3f6b2f;
    --rose-pink: #e07a90;
    --rose-blush: #f5c3c3;
    --peach: #f0ad88;
  }
  * { margin: 0; padding: 0; box-sizing: border-box; }
  html, body { width: 1200px; height: 1200px; overflow: hidden; }
  body { background: var(--backdrop); position: relative; }

  .box-front {
    position: absolute;
    left: 322px; top: 90px;
    width: 556px; height: 1020px;
    background: var(--box-white);
    overflow: hidden;
    box-shadow: 0 10px 30px rgba(0,0,0,0.08);
  }

  .floral { position: absolute; }

  .floral--top {
    left: -20px; top: -20px; width: 600px; height: 200px;
    border-radius: 0 0 55% 45% / 0 0 60% 40%;
    background:
      linear-gradient(100deg,
        var(--petal-cream) 0%, var(--petal-white) 12%,
        var(--peach) 16%, var(--rose-blush) 27%, var(--petal-white) 34%,
        var(--leaf-light) 42%, var(--petal-white) 50%,
        var(--leaf-green) 60%, var(--leaf-light) 70%,
        var(--petal-cream) 82%, var(--foil-gold) 90%, var(--petal-white) 100%);
  }
  .floral--right-upper {
    left: 440px; top: 120px; width: 150px; height: 330px;
    border-radius: 60% 0 0 55% / 40% 0 0 45%;
    background:
      linear-gradient(170deg,
        var(--leaf-green) 0%, var(--petal-cream) 22%,
        var(--leaf-light) 40%, var(--petal-white) 55%,
        var(--foil-gold) 68%, var(--leaf-green) 80%, var(--petal-white) 100%);
  }
  .floral--left-middle {
    left: -30px; top: 200px; width: 180px; height: 420px;
    border-radius: 0 55% 60% 0 / 0 45% 50% 0;
    background:
      linear-gradient(180deg,
        var(--leaf-light) 0%, var(--leaf-deep) 18%,
        var(--petal-white) 32%, var(--petal-cream) 48%,
        var(--petal-white) 62%, var(--foil-gold) 72%, var(--petal-white) 85%, var(--leaf-light) 100%);
  }
  .floral--right-lower {
    left: 400px; top: 520px; width: 190px; height: 330px;
    border-radius: 55% 0 0 60% / 45% 0 0 50%;
    background:
      linear-gradient(195deg,
        var(--petal-white) 0%, var(--petal-cream) 25%,
        var(--petal-white) 45%, var(--foil-gold) 58%,
        var(--petal-white) 72%, var(--petal-cream) 100%);
  }
  .floral--bottom-left {
    left: -20px; top: 610px; width: 230px; height: 430px;
    border-radius: 0 60% 40% 0 / 0 40% 30% 0;
    background:
      linear-gradient(180deg,
        var(--leaf-deep) 0%, var(--rose-blush) 12%, var(--leaf-green) 26%,
        var(--rose-pink) 40%, var(--rose-blush) 55%,
        var(--leaf-deep) 68%, var(--rose-blush) 80%, var(--leaf-green) 100%);
  }
  .floral--bottom-center {
    left: 180px; top: 900px; width: 400px; height: 140px;
    border-radius: 60% 40% 0 0 / 70% 50% 0 0;
    background:
      linear-gradient(90deg,
        var(--petal-white) 0%, var(--leaf-light) 18%, var(--petal-cream) 35%,
        var(--leaf-green) 52%, var(--petal-white) 68%, var(--foil-gold) 78%,
        var(--leaf-deep) 92%, var(--leaf-green) 100%);
  }

  .name-frame {
    position: absolute;
    left: 95px; top: 181px; width: 398px; height: 326px;
    border: 2px solid var(--frame-line);
    background: var(--box-white);
    text-align: center;
    color: var(--ink);
  }
  .name-frame__line {
    display: block;
    font-family: "Josefin Sans", sans-serif;
    font-weight: 300;
    font-size: 68px;
    line-height: 1;
  }
  .name-frame__line--first { margin-top: 18px; }
  .name-frame__line--second { margin-top: 30px; }
  .name-frame__accent {
    display: block;
    font-family: "Kaushan Script", cursive;
    font-size: 98px;
    line-height: 1;
    margin-top: 10px;
  }

  .product-details {
    position: absolute;
    left: 0; width: 556px; top: 770px;
    padding-left: 22px;
    text-align: center;
    color: var(--ink);
  }
  .product-details__label {
    font-family: "Kaushan Script", cursive;
    font-size: 38px;
    line-height: 1;
  }
  .product-details__volume {
    font-family: "Kaushan Script", cursive;
    font-size: 20px;
    margin-top: 6px;
  }
</style>
</head>
<body>
  <main class="box-front">
    <div class="floral floral--top" role="img" aria-label="Peach roses, white jasmine and green leaves along the top edge"></div>
    <div class="floral floral--right-upper" role="img" aria-label="Freesia and white blossoms with leaves on the upper right"></div>
    <div class="floral floral--left-middle" role="img" aria-label="White jasmine and lily of the valley on the left side"></div>
    <div class="floral floral--right-lower" role="img" aria-label="White gardenia and freesia on the lower right"></div>
    <div class="floral floral--bottom-left" role="img" aria-label="Pink roses with dark green leaves in the lower left corner"></div>
    <div class="floral floral--bottom-center" role="img" aria-label="Lily of the valley sprigs along the bottom edge"></div>

    <div class="name-frame">
      <span class="name-frame__line name-frame__line--first">Your</span>
      <span class="name-frame__line name-frame__line--second">Company</span>
      <span class="name-frame__accent">Name</span>
    </div>

    <div class="product-details">
      <div class="product-details__label">Details</div>
      <div class="product-details__volume">20/ml</div>
    </div>
  </main>
</body>
</html>
```